Customizable natural skin care line needs a product labels and logo design

We need product labels designed for plant based multitasking products with customizable options They are simple basic products that can be mixed at home,used in a way thats is beyond their intended function delivering a unique benefits Our Personalized and seasonal beauty offers versatility We are introducing 4 basic products ,6 additives with botanical extracts that help balance,nourish ,protect correct,energies and revive the skin and 2 seasonal products . Our products will help people address their own skin concerns and provide longer shelf life /Our products are safe for the environment and skin health and we like to see clean and simple Eco Labels Labels - that should communicate fresh,simple,fewer ingredients multi purpose. easy to mix

Target Market(s)

35 and up

Logo Text

Customize it ... blend ... mix .... Doesn’t have to have a text .. ?

Font styles to use
Serif

Colors

Designer to choose only greyscale colors for use in the design.

Requirements
Must have
• Most importantly is to know is that there are 2 different set of products that can be used as they are or enhanced with the other botanical additives ..customizable
for the products to give impression that they go together
The first set are the Basics ... second set treatment essence .. I open for new names
Nice to have
• Simple one color design easy to remember clean organic fresh

```html
<!DOCTYPE html>
<html lang="en">
<head>
<meta charset="utf-8">
<title>Botanical Product Labels</title>
<link href="https://fonts.googleapis.com/css2?family=Cormorant+Garamond:wght@300;400&family=EB+Garamond:wght@400;600&family=Playfair+Display:wght@700&display=swap" rel="stylesheet">
<style>
  :root {
    --backdrop-light: #f1f1f1;
    --backdrop-dark: #dcdcdc;
    --label-white: #ffffff;
    --label-edge: #d2d2d2;
    --ring: #c4c4c4;
    --brand-ink: #2e2e2e;
    --heading-ink: #4a4a4a;
    --body-ink: #555555;
    --net-ink: #444444;
    --foliage-light: rgba(190, 190, 190, 0.40);
    --foliage-deep: rgba(150, 150, 150, 0.32);
    --band-balance: #9a9a9a;
    --band-nourish: #8a8a8a;
    --band-protect: #7a7a7a;
    --band-energies: #6a6a6a;
    --band-seasonal-one: #585858;
    --band-seasonal-two: #464646;
  }
  html, body {
    margin: 0;
    padding: 0;
    width: 1200px;
    height: 843px;
    overflow: hidden;
  }
  body {
    background: radial-gradient(ellipse at 50% 45%, var(--backdrop-light) 0%, var(--backdrop-dark) 100%);
    position: relative;
  }
  .label {
    position: absolute;
    width: 274px;
    height: 274px;
    border-radius: 50%;
    background: var(--label-white);
    box-shadow: 0 0 0 1px var(--label-edge);
    overflow: hidden;
  }
  .label__foliage {
    position: absolute;
    left: 60px;
    top: 140px;
    width: 240px;
    height: 150px;
    background:
      radial-gradient(ellipse at 75% 40%, var(--foliage-deep) 0%, transparent 45%),
      radial-gradient(ellipse at 40% 90%, var(--foliage-deep) 0%, transparent 40%),
      radial-gradient(ellipse at 55% 60%, var(--foliage-light) 0%, transparent 70%);
  }
  .label__ring {
    position: absolute;
    left: 6px;
    top: 6px;
    width: 258px;
    height: 258px;
    border-radius: 50%;
    border: 2.5px solid var(--ring);
  }
  .label__brand, .label__tagline, .label__heading, .label__ingredients, .label__net {
    position: absolute;
    left: 0;
    width: 274px;
    text-align: center;
    white-space: nowrap;
  }
  .label__brand {
    top: 52px;
    font: 700 22px/28px "Playfair Display", serif;
    letter-spacing: 0.5px;
    color: var(--brand-ink);
  }
  .label__tagline {
    top: 76px;
    font: 600 15px/18px "EB Garamond", serif;
    color: var(--brand-ink);
  }
  .label__band {
    position: absolute;
    left: 20px;
    top: 100px;
    width: 234px;
    height: 36px;
    clip-path: polygon(0 100%, 1.5% 0, 98.5% 0, 100% 100%);
    color: var(--label-white);
    font: 300 34px/36px "Cormorant Garamond", serif;
    letter-spacing: 5px;
    text-align: center;
    white-space: nowrap;
  }
  .label__band--tight {
    letter-spacing: 1px;
    font-size: 32px;
  }
  .label__band--balance { background: var(--band-balance); }
  .label__band--nourish { background: var(--band-nourish); }
  .label__band--protect { background: var(--band-protect); }
  .label__band--energies { background: var(--band-energies); }
  .label__band--seasonal-one { background: var(--band-seasonal-one); }
  .label__band--seasonal-two { background: var(--band-seasonal-two); }
  .label__heading {
    top: 147px;
    font: 600 11px/13px "EB Garamond", serif;
    letter-spacing: 0.6px;
    color: var(--heading-ink);
  }
  .label__ingredients {
    top: 162px;
    font: 400 9px/9.7px "EB Garamond", serif;
    color: var(--body-ink);
  }
  .label__net {
    top: 237px;
    font: 400 9px/11px "EB Garamond", serif;
    color: var(--net-ink);
  }
</style>
</head>
<body>

<div class="label" style="left:73px; top:110px;">
  <div class="label__foliage" role="img" aria-label="Soft watercolour leaves"></div>
  <div class="label__ring"></div>
  <div class="label__brand">YOUR BRAND</div>
  <div class="label__tagline">brand tagline</div>
  <div class="label__band label__band--balance">balance</div>
  <div class="label__heading">INGREDIENTS :</div>
  <div class="label__ingredients">Lorem ipsum dolor sit amet, consectetur adipisicing elit,<br>sed do eiusmod tempor incididunt ut labore et dolore<br>magna aliqua. Ut enim ad minim veniam, quis nostrud<br>exercitation ullamco laboris nisi ut aliquip ex ea<br>commodo consequat. Duis aute irure dolor in<br>reprehenderit in voluptate velit esse cillum<br>dolore eu fugiat nulla pariatur</div>
  <div class="label__net">Net Wt. 123 oz (123gr)</div>
</div>

<div class="label" style="left:385px; top:110px;">
  <div class="label__foliage" role="img" aria-label="Soft watercolour leaves"></div>
  <div class="label__ring"></div>
  <div class="label__brand">YOUR BRAND</div>
  <div class="label__tagline">brand tagline</div>
  <div class="label__band label__band--nourish">nourish</div>
  <div class="label__heading">INGREDIENTS :</div>
  <div class="label__ingredients">Lorem ipsum dolor sit amet, consectetur adipisicing elit,<br>sed do eiusmod tempor incididunt ut labore et dolore<br>magna aliqua. Ut enim ad minim veniam, quis nostrud<br>exercitation ullamco laboris nisi ut aliquip ex ea<br>commodo consequat. Duis aute irure dolor in<br>reprehenderit in voluptate velit esse cillum<br>dolore eu fugiat nulla pariatur</div>
  <div class="label__net">Net Wt. 123 oz (123gr)</div>
</div>

<div class="label" style="left:697px; top:110px;">
  <div class="label__foliage" role="img" aria-label="Soft watercolour leaves"></div>
  <div class="label__ring"></div>
  <div class="label__brand">YOUR BRAND</div>
  <div class="label__tagline">brand tagline</div>
  <div class="label__band label__band--protect label__band--tight">protect correct</div>
  <div class="label__heading">INGREDIENTS :</div>
  <div class="label__ingredients">Lorem ipsum dolor sit amet, consectetur adipisicing elit,<br>sed do eiusmod tempor incididunt ut labore et dolore<br>magna aliqua. Ut enim ad minim veniam, quis nostrud<br>exercitation ullamco laboris nisi ut aliquip ex ea<br>commodo consequat. Duis aute irure dolor in<br>reprehenderit in voluptate velit esse cillum<br>dolore eu fugiat nulla pariatur</div>
  <div class="label__net">Net Wt. 123 oz (123gr)</div>
</div>

<div class="label" style="left:229px; top:421px;">
  <div class="label__foliage" role="img" aria-label="Soft watercolour leaves"></div>
  <div class="label__ring"></div>
  <div class="label__brand">YOUR BRAND</div>
  <div class="label__tagline">brand tagline</div>
  <div class="label__band label__band--energies">energies</div>
  <div class="label__heading">INGREDIENTS :</div>
  <div class="label__ingredients">Lorem ipsum dolor sit amet, consectetur adipisicing elit,<br>sed do eiusmod tempor incididunt ut labore et dolore<br>magna aliqua. Ut enim ad minim veniam, quis nostrud<br>exercitation ullamco laboris nisi ut aliquip ex ea<br>commodo consequat. Duis aute irure dolor in<br>reprehenderit in voluptate velit esse cillum<br>dolore eu fugiat nulla pariatur</div>
  <div class="label__net">Net Wt. 123 oz (123gr)</div>
</div>

<div class="label" style="left:541px; top:421px;">
  <div class="label__foliage" role="img" aria-label="Soft watercolour leaves"></div>
  <div class="label__ring"></div>
  <div class="label__brand">YOUR BRAND</div>
  <div class="label__tagline">brand tagline</div>
  <div class="label__band label__band--seasonal-one">seasonal 1</div>
  <div class="label__heading">INGREDIENTS :</div>
  <div class="label__ingredients">Lorem ipsum dolor sit amet, consectetur adipisicing elit,<br>sed do eiusmod tempor incididunt ut labore et dolore<br>magna aliqua. Ut enim ad minim veniam, quis nostrud<br>exercitation ullamco laboris nisi ut aliquip ex ea<br>commodo consequat. Duis aute irure dolor in<br>reprehenderit in voluptate velit esse cillum<br>dolore eu fugiat nulla pariatur</div>
  <div class="label__net">Net Wt. 123 oz (123gr)</div>
</div>

<div class="label" style="left:853px; top:421px;">
  <div class="label__foliage" role="img" aria-label="Soft watercolour leaves"></div>
  <div class="label__ring"></div>
  <div class="label__brand">YOUR BRAND</div>
  <div class="label__tagline">brand tagline</div>
  <div class="label__band label__band--seasonal-two">seasonal 2</div>
  <div class="label__heading">INGREDIENTS :</div>
  <div class="label__ingredients">Lorem ipsum dolor sit amet, consectetur adipisicing elit,<br>sed do eiusmod tempor incididunt ut labore et dolore<br>magna aliqua. Ut enim ad minim veniam, quis nostrud<br>exercitation ullamco laboris nisi ut aliquip ex ea<br>commodo consequat. Duis aute irure dolor in<br>reprehenderit in voluptate velit esse cillum<br>dolore eu fugiat nulla pariatur</div>
  <div class="label__net">Net Wt. 123 oz (123gr)</div>
</div>

</body>
</html>
```